SEAFOOD PACKAGING (Products for consumer)

We are looking to create packaging for various seafood products such as octopus and squid. We plan to sell our products in upscale supermarkets.

We are specializing in cut octopus this time.

Please include our company logo. Also, please leave a transparent area so that customers can see the product inside.
Updates

We want to show what is inside, so a picture of the octopus is not required. We need something simple and sophisticated.

Target Market(s)

upscale store in US and ASIA

Industry/Entity Type

Fisheries dealer

Requirements
Must have
• Please include the attached logo,Blue one is preferred.Please leave a transparent part so that the contents of the product can be seen by the consumer.1. product name on packaging →CUT OCTOPUS,TAKO SASHIMI,Highest quality,Top quality etc... 3. What text information should be on the packaging →(It may be edited, but this is the image) The raw materials are caught in a very clean environment and processed in a modern factory with ZEK certification. We are committed to additive-free products. 4. Packing size(cm/inch)→it will be about 19cm*22cm. 5. what kind of packaging do you use →PP or PA 6. dll →ai,jag
Nice to have
• https://quillmora.example/shots/4829174-Velka-Reef We need something simple and sophisticated like this one.
Should not have
• We want to show what is inside, so a picture of the octopus is not required. We need something simple and sophisticated.

```html
<!DOCTYPE html>
<html lang="en">
<head>
<meta charset="UTF-8">
<title>Marlow Cut Octopus – Tako Sashimi Pack Front</title>
<link href="https://fonts.googleapis.com/css2?family=Josefin+Sans:wght@400;600;700&display=swap" rel="stylesheet">
<style>
  :root {
    --stage: #4a4b4d;
    --brand-blue: #1c59a6;
    --deep-blue: #174c90;
    --window-gray: #c6c7c9;
    --paper: #fbfafa;
    --white: #ffffff;
    --plate-dark: #262d3a;
    --plate-mid: #4a5466;
    --flesh: #e9d4cf;
  }
  * { margin: 0; padding: 0; box-sizing: border-box; }
  html, body {
    width: 1200px; height: 900px; overflow: hidden;
    background: var(--stage);
    font-family: "Josefin Sans", sans-serif;
  }
  .pack-front {
    position: absolute; left: 246px; top: 40px;
    width: 708px; height: 820px; overflow: hidden;
  }
  .pack-shapes { position: absolute; inset: 0; }
  .brand-lockup {
    position: absolute; top: 78px; left: 0; width: 708px;
    display: flex; justify-content: center; align-items: center; gap: 18px;
  }
  .brand-dot {
    width: 58px; height: 58px; border-radius: 50%;
    background: var(--brand-blue);
  }
  .brand-name {
    color: var(--brand-blue); font-weight: 700; font-size: 78px;
    letter-spacing: 6px; line-height: 1; padding-top: 10px;
  }
  .product-name, .product-sub, .claims {
    position: absolute; left: 0; width: 708px; text-align: center;
    color: var(--white); text-transform: uppercase;
  }
  .product-name { top: 194px; font-size: 76px; font-weight: 600; letter-spacing: 2px; line-height: 1; }
  .product-sub { top: 266px; font-size: 52px; font-weight: 600; letter-spacing: 1px; line-height: 1; }
  .claims {
    top: 326px; font-size: 17px; font-weight: 400; letter-spacing: 1px;
    display: flex; justify-content: center; gap: 22px;
  }
  .claims .sep { font-weight: 700; }
  .story {
    position: absolute; left: 57px; top: 697px; width: 370px;
    color: var(--white); font-size: 10.5px; letter-spacing: 0.4px;
    text-transform: uppercase; line-height: 16px;
  }
  .story-rule { border: 0; border-top: 1.5px solid var(--white); margin: 3px 0 4px; width: 366px; }
  .net-weight {
    position: absolute; left: 57px; top: 771px;
    color: var(--white); font-size: 17px; letter-spacing: 0.6px; text-transform: uppercase;
  }
</style>
</head>
<body>
  <div class="pack-front">
    <svg class="pack-shapes" viewBox="0 0 708 820" width="708" height="820">
      <defs>
        <radialGradient id="plate-tones" cx="0.45" cy="0.5" r="0.55">
          <stop offset="0" stop-color="var(--flesh)"/>
          <stop offset="0.45" stop-color="#c98a80"/>
          <stop offset="0.75" stop-color="var(--plate-mid)"/>
          <stop offset="1" stop-color="var(--plate-dark)"/>
        </radialGradient>
      </defs>
      <rect class="body-blue" width="708" height="820" fill="var(--brand-blue)"/>
      <path class="top-label" d="M0 0 H708 V112 Q354 218 0 125 Z" fill="var(--paper)"/>
      <rect class="window-edge" x="0" y="355" width="708" height="6" fill="var(--white)"/>
      <rect class="product-window" x="0" y="361" width="708" height="330" fill="var(--window-gray)"/>
      <path class="info-band" d="M0 672 C20 672 36 648 72 648 C108 648 124 672 144 672 C164 672 180 648 216 648 C252 648 268 672 288 672 C308 672 324 648 360 648 C396 648 412 672 432 672 C452 672 468 648 504 648 C540 648 556 672 576 672 C596 672 612 648 648 648 C684 648 700 672 720 672 V830 H0 Z" fill="var(--deep-blue)" stroke="var(--white)" stroke-width="5"/>
      <circle class="serving-photo" cx="642" cy="609" r="215" fill="url(#plate-tones)" role="img" aria-label="Photo of sliced octopus sashimi on a dark plate with green leaves"/>
    </svg>

    <div class="brand-lockup">
      <span class="brand-dot"></span>
      <span class="brand-name">MARLOW</span>
    </div>

    <h1 class="product-name">Cut Octopus</h1>
    <h2 class="product-sub">Tako Sashimi</h2>
    <p class="claims"><span>All Natural</span><span class="sep">•</span><span>No Preservatives</span><span class="sep">•</span><span>No Additives</span></p>

    <div class="story">
      <p>The raw materials are caught in a very clean environment and processed in a modern factory with ZEK certification</p>
      <hr class="story-rule">
      <p>We are committed to additive-free products</p>
    </div>
    <p class="net-weight">Net Wt 16oz (1lb) 454g</p>
  </div>
</body>
</html>
```